Business card design for holistic health care clinic

We need a double-sided business card design for our holistic health care clinic that integrates our logo design and also its color scheme. My business is called Veluma. It is an integrative medicine clinic. You have already done the logo for me. Please ensure an elegant and upscale design that is not cluttered, but still has all the necessary information (please see below for details).

Target Market(s)

Wellness, fitness, rehabilitation for educated, well-traveled open-minded clients who are focused on natural, organic, balanced and preventive healthcare and lifestyle.

Industry/Entity Type

Medical

Contact Information for Business Card

Modern, clean.

Number of Pages Required

1 page

Font styles to use
Serif
Sans Serif

Colors

Designer to choose colors to be used in the design.

Requirements
Must have
• Logo on one side, all other information on the other side.
• Other information should include:
• Tomas Brevik - DOE, CPT, LMT
• 4120 North Harlow Street
• Austin, TX 78631
• 512 608 2947
• 818 459 7208
• info@VelumaHealth.com
• t.brevik@VelumaHealth.com
Nice to have
• Darker background on front - but not totally black - shaded/dark gray.

```html
<!DOCTYPE html>
<html lang="en">
<head>
<meta charset="utf-8">
<title>Veluma – Business Card</title>
<link rel="stylesheet" href="https://fonts.googleapis.com/css2?family=Nunito+Sans:wght@400;600;800&display=swap">
<style>
  :root {
    --backdrop: #e9eaec;
    --brand-blue: #0b90d1;
    --accent-blue: #1a9ee0;
    --ink-dark: #1d2a35;
    --card-dark: #1b1c1e;
    --shadow: rgba(0, 0, 0, 0.22);
  }
  * { box-sizing: border-box; margin: 0; padding: 0; }
  html, body {
    width: 1200px; height: 780px; overflow: hidden;
    background: var(--backdrop);
    font-family: "Nunito Sans", Arial, sans-serif;
  }
  .canvas {
    width: 1200px; height: 780px;
    display: flex; align-items: center; justify-content: center; gap: 40px;
  }
  .card {
    width: 560px; height: 320px; border-radius: 4px;
    box-shadow: 0 12px 30px var(--shadow);
    position: relative; overflow: hidden;
  }

  /* Front side */
  .card-front {
    background: var(--brand-blue);
    display: flex; align-items: center; justify-content: center;
  }
  .brand-lockup { display: flex; flex-direction: column; align-items: center; }
  .brand-name {
    font-weight: 800; font-size: 70px; letter-spacing: 1px;
    text-transform: uppercase; color: var(--ink-dark); line-height: 1;
  }
  .brand-tagline {
    margin-top: 6px; font-weight: 600; font-size: 17px;
    color: var(--ink-dark); letter-spacing: 0.3px;
  }

  /* Back side */
  .card-back {
    background: var(--card-dark);
    display: flex; align-items: center; padding: 0 28px;
  }
  .card-back .brand-lockup { width: 255px; }
  .card-back .brand-name { color: var(--accent-blue); font-size: 50px; }
  .card-back .brand-tagline { color: var(--accent-blue); font-size: 12.5px; }
  .divider {
    width: 1.5px; height: 210px; background: var(--accent-blue);
    margin: 0 22px 0 18px;
  }
  .contact { color: var(--accent-blue); }
  .person-name { font-weight: 800; font-size: 17px; text-transform: uppercase; line-height: 1.1; }
  .person-title { font-size: 13px; letter-spacing: 0.5px; margin-bottom: 14px; }
  .contact-list { list-style: none; font-size: 13px; line-height: 1.85; }
  .contact-list li { display: flex; align-items: center; gap: 8px; }
  .contact-icon { width: 15px; height: 15px; flex: none; }
  .address { margin-top: 6px; font-size: 13px; line-height: 1.4; }
</style>
</head>
<body>
<main class="canvas">

  <section class="card card-front" aria-label="Card front">
    <div class="brand-lockup">
      <span class="brand-name">Veluma</span>
      <span class="brand-tagline">Integrative Holistic Medicine</span>
    </div>
  </section>

  <section class="card card-back" aria-label="Card back">
    <div class="brand-lockup">
      <span class="brand-name">Veluma</span>
      <span class="brand-tagline">Integrative Holistic Medicine</span>
    </div>
    <div class="divider"></div>
    <div class="contact">
      <p class="person-name">Tomas Brevik</p>
      <p class="person-title">DOE, CPT, LMT</p>
      <ul class="contact-list">
        <li>
          <svg class="contact-icon" viewBox="0 0 16 16" aria-hidden="true"><circle cx="8" cy="8" r="7.2" fill="none" stroke="currentColor" stroke-width="1.2"/><rect x="5.5" y="3.8" width="5" height="8.4" rx="1" fill="none" stroke="currentColor" stroke-width="1.1"/></svg>
          512 608 2947
        </li>
        <li>
          <svg class="contact-icon" viewBox="0 0 16 16" aria-hidden="true"><circle cx="8" cy="8" r="7.2" fill="none" stroke="currentColor" stroke-width="1.2"/><path d="M5.2 4.5l1.6-.4.9 2-1 .8c.5 1.1 1.3 1.9 2.4 2.4l.8-1 2 .9-.4 1.6c-3.3.3-6.6-3-6.3-6.3z" fill="currentColor"/></svg>
          818 459 7208
        </li>
        <li>
          <svg class="contact-icon" viewBox="0 0 16 16" aria-hidden="true"><circle cx="8" cy="8" r="7.2" fill="none" stroke="currentColor" stroke-width="1.2"/><rect x="4" y="5.2" width="8" height="5.6" fill="none" stroke="currentColor" stroke-width="1.1"/><path d="M4 5.4l4 3 4-3" fill="none" stroke="currentColor" stroke-width="1.1"/></svg>
          info@VelumaHealth.com
        </li>
        <li>
          <svg class="contact-icon" viewBox="0 0 16 16" aria-hidden="true"><circle cx="8" cy="8" r="7.2" fill="none" stroke="currentColor" stroke-width="1.2"/><rect x="4" y="5.2" width="8" height="5.6" fill="none" stroke="currentColor" stroke-width="1.1"/><path d="M4 5.4l4 3 4-3" fill="none" stroke="currentColor" stroke-width="1.1"/></svg>
          t.brevik@VelumaHealth.com
        </li>
      </ul>
      <p class="address">4120 North Harlow Street<br>Austin, TX 78631</p>
    </div>
  </section>

</main>
</body>
</html>
```